Kickass billboard for motorway

Fix my old hauler - clue is in the name.
We have a 45ft billboard we're looking to design constructed from an old trailer we own (so we can be as creative as possible).
We provide a van buying service, being one of the only companies in the UK with the facilities to recover faulty, damaged and broken vans - from small car derived vans to large trucks and lorries.
ur niche in the market is different to car buying services, as buying and selling cars is often an emotionally driven process, whereas people often see and treat vans purely as a tool. There are alternatives to a car, public transport etc, but not to a work van - so people go out straight away and replace them immediately, often leaving the old broken van to sit on their drive or in their unit.
Looking to start building a brand asset bank.
Feel free to check out our website to get a feel for what we do:
Fixmyoldhauler.co.uk

Target Market(s)

Van owners/drivers & fleet managers

Industry/Entity Type

Automotive

Font styles to use
Sans Serif

Colors
34a7d8

Requirements
Must have
• Eye-catching - very eye-catching.
We want to advertise the fact we collect vehicles for free.
We pay instantly upon arrival.
Our phone number 0161 493 7062
Our website www.fixmyoldhauler.co.uk
Nice to have
• 3d elements - we have the ability to get 3d props for the billboard including damaged vans etc.

```html
<!DOCTYPE html>
<html lang="en">
<head>
<meta charset="utf-8">
<title>Fix my old hauler – Billboard</title>
<link rel="stylesheet" href="https://fonts.googleapis.com/css2?family=Montserrat:wght@500;600;700;800&display=swap">
<style>
  :root {
    --brand-blue: #34a7d8;
    --ink: #231f20;
    --paper: #ffffff;
    --van-teal: #5fc7c4;
    --van-teal-dark: #3a9ea0;
  }
  * { margin: 0; padding: 0; box-sizing: border-box; }
  html, body {
    width: 874px;
    height: 1200px;
    overflow: hidden;
    background: var(--paper);
    font-family: "Montserrat", Arial, sans-serif;
  }
  .billboard {
    position: absolute;
    left: 37px;
    top: 400px;
    width: 800px;
    height: 400px;
    background: var(--brand-blue);
    overflow: hidden;
    box-shadow: 8px 10px 18px rgba(0,0,0,0.35);
  }
  .billboard__corner {
    position: absolute;
    inset: 0;
    width: 800px;
    height: 352px;
  }
  .headline {
    position: absolute;
    left: 16px;
    top: 18px;
    font-size: 67px;
    font-weight: 700;
    letter-spacing: 1px;
    color: var(--ink);
    line-height: 1;
    white-space: nowrap;
  }
  .subline {
    position: absolute;
    left: 17px;
    top: 106px;
    font-size: 19.5px;
    font-weight: 600;
    letter-spacing: 1.6px;
    line-height: 27px;
    color: var(--paper);
  }
  .promise {
    position: absolute;
    left: 16px;
    top: 183px;
    font-size: 35px;
    font-weight: 700;
    letter-spacing: 0.5px;
    line-height: 42px;
    color: var(--paper);
  }
  .van-visual {
    position: absolute;
    left: 386px;
    top: 96px;
    width: 400px;
    height: 212px;
    border-radius: 40px 60px 20px 30px;
    background: radial-gradient(ellipse at 55% 45%, var(--van-teal) 0%, var(--van-teal-dark) 70%, rgba(58,158,160,0) 100%);
  }
  .contact-bar {
    position: absolute;
    left: 0;
    bottom: 0;
    width: 800px;
    height: 48px;
    display: flex;
  }
  .contact-bar__phone {
    width: 421px;
    background: var(--ink);
    display: flex;
    align-items: center;
    padding-left: 17px;
    gap: 12px;
  }
  .contact-bar__divider {
    width: 3px;
    background: var(--brand-blue);
  }
  .contact-bar__web {
    flex: 1;
    background: var(--ink);
    display: flex;
    align-items: center;
    padding-left: 10px;
  }
  .call-now {
    font-size: 15px;
    font-weight: 700;
    line-height: 14px;
    color: var(--paper);
  }
  .phone-number {
    font-size: 40px;
    font-weight: 700;
    letter-spacing: 0.5px;
    color: var(--paper);
    line-height: 1;
    white-space: nowrap;
  }
  .web-address {
    font-size: 17px;
    font-weight: 700;
    color: var(--paper);
    white-space: nowrap;
  }
</style>
</head>
<body>
  <section class="billboard">
    <svg class="billboard__corner" viewBox="0 0 800 352" aria-hidden="true">
      <polygon points="754,0 800,0 800,352 458,352" fill="#ffffff"/>
    </svg>

    <h1 class="headline">SELL YOUR VAN</h1>
    <p class="subline">We want to advertise the fact<br>we collect vehicles for free.</p>
    <p class="promise">WE PAY INSTANTLY<br>UPON ARRIVAL.</p>

    <div class="van-visual" role="img" aria-label="Photo of a teal minivan with a crushed front end and cracked windscreen"></div>

    <div class="contact-bar">
      <div class="contact-bar__phone">
        <span class="call-now">CALL<br>NOW!</span>
        <span class="phone-number">0161 493 7062</span>
      </div>
      <div class="contact-bar__divider"></div>
      <div class="contact-bar__web">
        <span class="web-address">WWW.FIXMYOLDHAULER.CO.UK</span>
      </div>
    </div>
  </section>
</body>
</html>
```